Thornwell Building Company - advertisement poster

I am looking to print some canvas signs to advertise my general contracting company, Thornwell Building Company. The sign will measure 6' long x 3' high so the size should match that ratio. I already have a logo icon, which is the Letter 'A' and some trees that I would like to incorporate, see attached. I would also like the to have the following information listed:
1) phone number: 472-318-6095
2) email: thornwellbuildingcompany@mailvistra.net
3) website: thornwellbuildingcompany.com
4) Lic#5386204
5) I want to use this text: "BUILD WITH THE T-CREW!"

The ad should be relatively simple and clean. Black and Green are my company colors. I am open to creative ideas!

Target Market(s)

People looking to renovate their homes

Industry/Entity Type

Construction

Colors
59FF00
82FF00
B8FF75
E3FFCB
F4FFEA

Requirements
Must have
• Must have my company logo
Should not have
• No photos or complex graphics

```html
<!DOCTYPE html>
<html lang="en">
<head>
<meta charset="utf-8">
<title>Thornwell Building Company – Sign</title>
<link rel="stylesheet" href="https://fonts.googleapis.com/css2?family=Heebo:wght@400;500;700;800&display=swap">
<style>
  :root {
    --backdrop: #e6e8ea;
    --sign-black: #000000;
    --brand-green: #6db647;
    --ink-white: #ffffff;
    --ink-dark: #0a0a0a;
  }
  * { margin: 0; padding: 0; box-sizing: border-box; }
  html, body {
    width: 1200px;
    height: 800px;
    overflow: hidden;
    background: var(--backdrop);
    font-family: "Heebo", Arial, sans-serif;
  }
  .sign {
    position: absolute;
    left: 40px;
    top: 120px;
    width: 1120px;
    height: 560px;
    background: var(--sign-black);
    overflow: hidden;
  }
  .green-panel {
    position: absolute;
    inset: 0;
    width: 1120px;
    height: 560px;
  }
  .brand {
    position: absolute;
    left: 88px;
    top: 112px;
    display: flex;
    align-items: center;
    gap: 14px;
  }
  .brand-mark {
    width: 22px;
    height: 22px;
    background: var(--brand-green);
  }
  .brand-name {
    color: var(--ink-white);
    font-weight: 800;
    font-size: 25px;
    letter-spacing: 1px;
    line-height: 1.1;
    text-transform: uppercase;
  }
  .tagline {
    position: absolute;
    left: 88px;
    top: 258px;
    line-height: 1;
  }
  .tagline-lead {
    display: block;
    color: var(--brand-green);
    font-weight: 700;
    font-size: 38px;
    letter-spacing: 0.5px;
  }
  .tagline-crew {
    display: block;
    margin-top: 4px;
    color: var(--ink-white);
    font-weight: 700;
    font-size: 64px;
    letter-spacing: 0.5px;
  }
  .licence {
    position: absolute;
    left: 92px;
    top: 438px;
    color: var(--brand-green);
    font-weight: 400;
    font-size: 22px;
  }
  .contact {
    position: absolute;
    left: 635px;
    top: 352px;
    list-style: none;
    color: var(--ink-dark);
  }
  .contact-item {
    display: flex;
    align-items: center;
    gap: 34px;
  }
  .contact-item svg { width: 22px; height: 22px; flex: none; }
  .contact-phone { font-weight: 700; font-size: 32px; height: 40px; }
  .contact-email, .contact-web { font-weight: 400; font-size: 21px; margin-top: 10px; }
</style>
</head>
<body>
  <main class="sign">
    <svg class="green-panel" viewBox="0 0 1120 560" aria-hidden="true">
      <polygon points="503,560 1120,560 1120,0 840,0 700,110 560,110 430,280 " fill="var(--brand-green)"/>
    </svg>

    <div class="brand">
      <span class="brand-mark"></span>
      <span class="brand-name">Thornwell Building Company</span>
    </div>

    <h1 class="tagline">
      <span class="tagline-lead">BUILD WITH THE</span>
      <span class="tagline-crew">T-CREW</span>
    </h1>

    <p class="licence">Lic#5386204Z</p>

    <ul class="contact">
      <li class="contact-item contact-phone">
        <svg viewBox="0 0 24 24" aria-hidden="true"><circle cx="12" cy="12" r="11" fill="var(--ink-dark)"/><rect x="8.5" y="5.5" width="7" height="13" rx="1.5" fill="none" stroke="var(--brand-green)" stroke-width="1.6"/></svg>
        <span>472-318-6095</span>
      </li>
      <li class="contact-item contact-email">
        <svg viewBox="0 0 24 24" aria-hidden="true"><circle cx="12" cy="12" r="10" fill="none" stroke="var(--ink-dark)" stroke-width="2"/><rect x="6.5" y="8" width="11" height="8" rx="1" fill="none" stroke="var(--ink-dark)" stroke-width="1.6"/><polyline points="6.5,8.5 12,12.5 17.5,8.5" fill="none" stroke="var(--ink-dark)" stroke-width="1.6"/></svg>
        <span>thornwellbuildingcompany@mailvistra.net</span>
      </li>
      <li class="contact-item contact-web">
        <svg viewBox="0 0 24 24" aria-hidden="true"><g fill="none" stroke="var(--ink-dark)" stroke-width="1.8"><circle cx="12" cy="12" r="10"/><ellipse cx="12" cy="12" rx="4.5" ry="10"/><line x1="2" y1="12" x2="22" y2="12"/><line x1="3.5" y1="7" x2="20.5" y2="7"/><line x1="3.5" y1="17" x2="20.5" y2="17"/></g></svg>
        <span>thornwellbuildingcompany.com</span>
      </li>
    </ul>
  </main>
</body>
</html>
```